WP website design (Whitcombe)

We need a wordpress design for an established auction and real estate company based in Daswon Creek, Canada. The winning design will incorporate a professional color scheme with company logo in a clean layout with specified widgets. The design needs to consider that this will be developed on a responsive theme. Colors will complement logo - red, black and gray.

Industry/Entity Type

Real Estate

Font styles to use
Sans Serif

Requirements
Must have
• Must Have:
the main logo is provided and the 'horse' logo shouldbe incorporated into the hearder or sidebar (either left or right)as well. Contact info should be placed in the header, and footer too: (250) 555-0147
(250) 555-0193
(250) 555-0128
lkr@fernvale-mail.example

- Navigation:
1) Home 2) Auctions 3) Online Auctions 4) About Us 5) Contact Us

Home Page will have following:
"Family owned and operated with a family guarantee.
Located in Ridgeford, B.C. Canada

Competitive Rates Bonded & Licensed Livestock Dealers & Auctioneers
All Types of Auction Sales in B.C. & Alberta

Farm, Machinery
Equipment Sales
Household & Estate Sales
Livestock Marketing Consultants
Field Cattle Sales
Livestock Pedigree Sales
Horse Sales Appraisals"

Homepage will have auctions - as at http://brindlegatesales.example/upcoming-auctions/.

Footer will have smaller company logo, credit card logo, and attached association logos and this contact info:
.(620) 555-0176: OFFICE
(620) 555-0134: FAX
vgroup@tqx.example: email
Address: 718 N. Birch Rd., Johnson KS
Mailing Address: PO Box 829, Larkvale, KS

Widgets:
1) email sign up 2) News blog widget 3) testimonial blog widget 4) featured auctions widget 5) the 'Gavel Row' logo which is included
Nice to have
• Nice to Have:
- demonstrate the drop-down menu styling, e.g. under Auctions
- Upcoming Auctions
- Past Auctions

```html
<!DOCTYPE html>
<html lang="en">
<head>
<meta charset="utf-8">
<title>Whitcombe's Auction Mart Ltd.</title>
<link rel="stylesheet" href="https://fonts.googleapis.com/css2?family=Open+Sans:wght@400;600;700&family=Oswald:wght@500;700&display=swap">
<style>
:root{
  --red:#c8161d;
  --red-dark:#8f0d12;
  --red-deep:#6e0a0e;
  --ink:#222;
  --text:#555;
  --muted:#888;
  --line:#dcdcdc;
  --panel:#f1f1f1;
  --dark:#2d2d2d;
  --white:#fff;
}
*{box-sizing:border-box;margin:0;padding:0}
html,body{width:1200px;height:2432px;overflow:hidden}
body{font-family:"Open Sans",Arial,sans-serif;color:var(--text);background:var(--white);position:relative;font-size:13px;line-height:1.5}
a{color:inherit;text-decoration:none}

/* header */
.site-header{position:absolute;left:0;top:0;width:1200px;height:124px}
.brand{position:absolute;left:80px;top:14px;width:190px;height:96px;display:flex;align-items:center;gap:12px}
.brand-mark{width:20px;height:20px;background:var(--red);flex:none}
.brand-name{font-family:"Oswald",Arial,sans-serif;font-weight:700;font-size:20px;line-height:1.05;color:var(--ink);text-transform:uppercase}
.header-contact{position:absolute;right:80px;top:12px;font-size:15px;color:var(--ink);line-height:1.45}
.header-contact strong{font-weight:700;display:block}
.header-contact .phone{color:var(--red);font-weight:600}

/* nav */
.main-nav{position:absolute;left:0;top:124px;width:1200px;height:36px;background:var(--red);border-bottom:3px solid var(--red-dark)}
.main-nav ul{list-style:none;position:absolute;left:80px;top:0;display:flex;height:33px}
.main-nav li{color:var(--white);font-size:13px;font-weight:700;text-transform:uppercase;padding:0 22px;line-height:33px;border-right:1px solid rgba(255,255,255,.25)}
.main-nav li.active{background:var(--red-dark)}
.nav-search{position:absolute;right:80px;top:6px;display:flex;align-items:center;gap:8px;color:var(--white);font-size:12px}
.nav-search span.box{display:block;width:150px;height:22px;background:var(--white);border-radius:2px}

/* hero */
.hero{position:absolute;left:80px;top:160px;width:1040px;height:380px;background:linear-gradient(135deg,#a8b1b8 0%,#d9d3c6 45%,#8e8b80 100%)}
.hero-dots{position:absolute;left:80px;top:514px;width:1040px;display:flex;justify-content:center;gap:8px}
.hero-dots i{width:10px;height:10px;border-radius:50%;background:rgba(255,255,255,.6)}
.hero-dots i.on{background:var(--white)}

/* main */
.main{position:absolute;left:80px;top:580px;width:720px}
h1.welcome{font-size:26px;font-weight:400;color:var(--ink);margin-bottom:10px}
h1.welcome em{font-style:normal;color:var(--red)}
.lead{font-size:13px;color:var(--text);margin-bottom:14px}
.facts p{font-size:13px;color:var(--ink);margin-bottom:2px}
.facts .hl{color:var(--red);font-weight:600;margin-top:12px}
.service-list{list-style:none;columns:2;margin-top:10px;width:560px}
.service-list li{font-size:13px;color:var(--ink);padding-left:16px;position:relative;margin-bottom:4px}
.service-list li::before{content:"";position:absolute;left:2px;top:8px;width:5px;height:5px;background:var(--red);border-radius:50%}

.featured{position:absolute;left:80px;top:930px;width:720px;height:1250px;background:var(--panel);border:1px solid var(--line);padding:16px 20px}
.featured h2{font-size:24px;font-weight:400;color:var(--ink);margin-bottom:6px}
.featured h2 em{font-style:normal;color:var(--red)}
.lot{background:var(--white);border:1px solid var(--line);margin-top:14px;height:354px;position:relative}
.lot-cat{font-size:14px;font-weight:700;color:var(--ink);padding:8px 14px;border-bottom:1px solid var(--line)}
.lot-photo{position:absolute;left:14px;top:50px;width:170px;height:130px;background:linear-gradient(160deg,#b9cbdc 0%,#e8e4da 55%,#7d9a63 100%)}
.lot-body{position:absolute;left:200px;top:48px;right:16px}
.lot-body h3{font-size:19px;font-weight:400;color:var(--red);margin-bottom:4px}
.lot-body p{font-size:12px;line-height:1.55;color:var(--text)}
.lot-btns{position:absolute;left:14px;top:196px;display:flex;gap:6px}
.btn{display:inline-block;font-size:11px;font-weight:700;text-transform:uppercase;padding:5px 14px;color:var(--white);background:var(--dark)}
.btn.red{background:var(--red)}
.lot-live{position:absolute;left:0;right:0;top:236px;border-top:1px solid var(--line);padding:12px 14px;background:#fafafa;height:116px}
.lot-live h4{font-size:17px;font-weight:600;color:var(--ink);margin-bottom:4px}
.lot-live p{font-size:12px;color:var(--text);line-height:1.6}
.lot-live p b{color:var(--red);font-weight:600}
.lot-live .bid{position:absolute;right:16px;top:30px;padding:7px 18px;background:var(--red);color:var(--white);font-size:11px;font-weight:700;text-transform:uppercase}
.pager{display:flex;gap:4px;margin-top:16px}
.pager span{border:1px solid var(--line);background:var(--white);font-size:11px;padding:3px 9px;color:var(--ink)}
.pager span.on{background:var(--red);color:var(--white);border-color:var(--red)}

/* sidebar */
.sidebar{position:absolute;left:820px;top:600px;width:300px}
.widget{border:1px solid var(--line);background:var(--white);margin-bottom:20px}
.widget-title{background:var(--red);color:var(--white);font-size:17px;font-weight:600;padding:8px 14px}
.widget-title.dark{background:var(--dark)}
.widget-body{padding:14px}
.field{height:30px;border:1px solid var(--line);font-size:12px;color:var(--muted);padding:6px 10px;margin-bottom:10px}
.signup{display:block;margin-left:auto;width:80px;text-align:center}
.quote{font-size:12px;line-height:1.55;padding-left:18px;position:relative;margin-bottom:12px}
.quote::before{content:"\201C";position:absolute;left:0;top:-4px;font-size:24px;color:var(--red);font-weight:700}
.quote cite{display:block;font-style:italic;color:var(--red);margin-top:3px}
.read-all{display:block;margin:4px auto 0;width:200px;text-align:center}
.news-item{border-bottom:1px solid var(--line);padding-bottom:10px;margin-bottom:10px}
.news-item:last-child{border-bottom:0;margin-bottom:0}
.news-item time{display:block;color:var(--red);font-weight:600;font-size:13px}
.news-item p{font-size:12px;line-height:1.55}
.news-item a{font-size:12px;color:var(--ink);font-weight:600}
.social{list-style:none}
.social li{display:flex;align-items:center;gap:12px;font-size:13px;color:var(--ink);padding:6px 0;border-bottom:1px solid #eee}
.social li:last-child{border-bottom:0}
.social li::before{content:"";width:24px;height:24px;border-radius:50%;background:var(--red);flex:none}

/* footer */
.site-footer{position:absolute;left:0;top:2200px;width:1200px;height:232px;background:var(--red-dark);color:#f1d6d6}
.footer-cols{position:absolute;left:80px;top:20px;display:flex;gap:44px}
.footer-cols h5{font-size:14px;color:var(--white);font-weight:700;margin-bottom:6px;line-height:1.4}
.footer-cols p,.footer-cols li{font-size:11.5px;line-height:1.7;list-style:none}
.assoc .assoc-row{display:flex;align-items:center;gap:10px;margin-bottom:12px}
.assoc .badge{width:70px;height:30px;background:#e9e9e9}
.assoc .nl{font-size:14px;font-weight:700;color:var(--white)}
.cards{display:flex;gap:6px}
.cards i{width:34px;height:22px;background:#e9e9e9;border-radius:2px}
.footer-brand{position:absolute;right:80px;top:24px;display:flex;align-items:center;gap:10px}
.footer-brand .brand-mark{background:var(--white);width:16px;height:16px}
.footer-brand .brand-name{color:var(--white);font-size:16px}
.footer-bottom{position:absolute;left:0;bottom:0;width:1200px;height:30px;background:var(--red-deep);font-size:11px;text-align:right;padding:7px 80px}
</style>
</head>
<body>

<header class="site-header">
  <div class="brand"><span class="brand-mark"></span><span class="brand-name">Whitcombe's Auction Mart Ltd.</span></div>
  <div class="header-contact">
    <strong>Contact Info:</strong>
    <span class="phone">(250) 555-0147</span> · <span class="phone">(250) 555-0193</span><br>
    <span class="phone">(250) 555-0128</span><br>
    Email: lkr@fernvale-mail.example
  </div>
</header>

<nav class="main-nav">
  <ul>
    <li class="active">Home</li>
    <li>Auctions</li>
    <li>Online Auctions</li>
    <li>About Us</li>
    <li>Contact Us</li>
  </ul>
  <div class="nav-search">Auction Search <span class="box"></span></div>
</nav>

<div class="hero" role="img" aria-label="Photo of a house with a red and yellow auction sign posted on the property"></div>
<div class="hero-dots"><i></i><i class="on"></i><i></i><i></i></div>

<main class="main">
  <h1 class="welcome">Welcome to <em>Whitcombe's Auction Mart Ltd.</em></h1>
  <p class="lead">Aliquam molestie, mi et imperdiet euismod, dui purus auctor tellus, at interdum lacus lectus at ante. Sed accumsan sollicitudin sapien, sit amet adipiscing turpis gravida ac.</p>
  <div class="facts">
    <p>Family owned and operated with a family guarantee.</p>
    <p>Located in Ridgeford, B.C. Canada</p>
    <p>Competitive Rates Bonded &amp; Licensed Livestock Dealers &amp; Auctioneers</p>
    <p class="hl">All Types of Auction Sales in B.C. &amp; Alberta</p>
  </div>
  <ul class="service-list">
    <li>Farm, Machinery</li>
    <li>Equipment Sales</li>
    <li>Household &amp; Estate Sales</li>
    <li>Livestock Marketing Consultants</li>
    <li>Field Cattle Sales</li>
    <li>Livestock Pedigree Sales</li>
    <li>Horse Sales Appraisals</li>
  </ul>
</main>

<section class="featured">
  <h2>Featured <em>Auctions</em></h2>

  <article class="lot">
    <div class="lot-cat">Real Estate Auction</div>
    <div class="lot-photo" role="img" aria-label="Photo of a two-storey residential home"></div>
    <div class="lot-body">
      <h3>Residential Home</h3>
      <p>Aliquam molestie, mi et imperdiet euismod, dui purus auctor tellus, at interdum lacus lectus at ante. Sed accumsan sollicitudin sapien, sit amet adipiscing turpis gravida ac. Integer lobortis nisi et nulla volutpat, libero mauris varius mi, vitae suscipit ipsum ligula vitae risus.</p>
    </div>
    <div class="lot-btns"><span class="btn">Details</span><span class="btn red">Photos</span></div>
    <div class="lot-live">
      <h4>Live On-Site Auction</h4>
      <p><b>Begin:</b> Saturday, October 25, 2013 at 10:00 AM EDT<br><b>Location:</b> 58 Harrow Lane<br>Millbrook Flats, ON K0X</p>
      <span class="bid">Click here for online bidding</span>
    </div>
  </article>

  <article class="lot">
    <div class="lot-cat">Real Estate Auction</div>
    <div class="lot-photo" role="img" aria-label="Photo of a residential home with a lawn"></div>
    <div class="lot-body">
      <h3>Residential Home</h3>
      <p>Aliquam molestie, mi et imperdiet euismod, dui purus auctor tellus, at interdum lacus lectus at ante. Sed accumsan sollicitudin sapien, sit amet adipiscing turpis gravida ac. Integer lobortis nisi et nulla volutpat, libero mauris varius mi, vitae suscipit ipsum ligula vitae risus.</p>
    </div>
    <div class="lot-btns"><span class="btn">Details</span><span class="btn red">Photos</span><span class="btn">Videos</span></div>
    <div class="lot-live">
      <h4>Live On-Site Auction</h4>
      <p><b>Begin:</b> Saturday, October 25, 2013 at 10:00 AM EDT<br><b>Location:</b> 58 Harrow Lane<br>Millbrook Flats, ON K0X</p>
      <span class="bid">Click here for online bidding</span>
    </div>
  </article>

  <article class="lot">
    <div class="lot-cat">Real Estate Auction</div>
    <div class="lot-photo" role="img" aria-label="Photo of a residential home under a blue sky"></div>
    <div class="lot-body">
      <h3>Residential Home</h3>
      <p>Aliquam molestie, mi et imperdiet euismod, dui purus auctor tellus, at interdum lacus lectus at ante. Sed accumsan sollicitudin sapien, sit amet adipiscing turpis gravida ac. Integer lobortis nisi et nulla volutpat, libero mauris varius mi, vitae suscipit ipsum ligula vitae risus.</p>
    </div>
    <div class="lot-btns"><span class="btn">Details</span><span class="btn red">Photos</span><span class="btn">Videos</span></div>
    <div class="lot-live">
      <h4>Live On-Site Auction</h4>
      <p><b>Begin:</b> Saturday, October 25, 2013 at 10:00 AM EDT<br><b>Location:</b> 58 Harrow Lane<br>Millbrook Flats, ON K0X</p>
      <span class="bid">Click here for online bidding</span>
    </div>
  </article>

  <div class="pager"><span>« Prev</span><span class="on">1</span><span>2</span><span>Next »</span></div>
</section>

<aside class="sidebar">
  <section class="widget">
    <div class="widget-title">E-Mail Sign Up</div>
    <div class="widget-body">
      <div class="field">Enter Email Address</div>
      <span class="btn red signup">Sign Up</span>
    </div>
  </section>

  <section class="widget">
    <div class="widget-title dark">Testimonials</div>
    <div class="widget-body">
      <p class="quote">Aliquam molestie, mi et imperdiet euismod, dui purus auctor tellus, at interdum lacus lectus at ante. Sed accumsan sollicitudin sapien, sit amet adipiscing turpis gravida ac.<cite>- Ellis Marden</cite></p>
      <p class="quote">Aliquam molestie, mi et imperdiet euismod, dui purus auctor tellus, at interdum lacus lectus at ante. Sed accumsan sollicitudin sapien, sit amet adipiscing turpis gravida ac.<cite>- Ellis Marden</cite></p>
      <span class="btn red read-all">Read all testimonials</span>
    </div>
  </section>

  <section class="widget">
    <div class="widget-title dark">News</div>
    <div class="widget-body">
      <div class="news-item"><time>May 25, 2014</time><p>Aliquam molestie, mi et imperdiet euismod, dui purus auctor tellus, at interdum lacus lectus at ante. Sed accumsan sollicitudin sapien, sit amet adipiscing turpis gravida ac.</p><a>Read more »</a></div>
      <div class="news-item"><time>May 25, 2014</time><p>Aliquam molestie, mi et imperdiet euismod, dui purus auctor tellus, at interdum lacus lectus at ante. Sed accumsan sollicitudin sapien, sit amet adipiscing turpis gravida ac.</p><a>Read more »</a></div>
      <div class="news-item"><time>May 25, 2014</time><p>Aliquam molestie, mi et imperdiet euismod, dui purus auctor tellus, at interdum lacus lectus at ante. Sed accumsan sollicitudin sapien, sit amet adipiscing turpis gravida ac.</p><a>Read more »</a></div>
      <div class="news-item"><time>May 25, 2014</time><p>Aliquam molestie, mi et imperdiet euismod, dui purus auctor tellus, at interdum lacus lectus at ante. Sed accumsan sollicitudin sapien, sit amet adipiscing turpis gravida ac.</p><a>Read more »</a></div>
    </div>
  </section>

  <section class="widget">
    <div class="widget-title dark">Connect us</div>
    <div class="widget-body">
      <ul class="social">
        <li>Friendpage</li>
        <li>Chirpline</li>
        <li>Worklink</li>
        <li>Pinboardly</li>
      </ul>
    </div>
  </section>
</aside>

<footer class="site-footer">
  <div class="footer-cols">
    <div>
      <h5>Company</h5>
      <ul><li>Home</li><li>Auctions</li><li>Online Auctions</li><li>About Us</li><li>Contact Us</li></ul>
    </div>
    <div>
      <h5>Contact Info</h5>
      <p>Address: 718 N. Birch Rd., Larkvale KS<br>Mailing Address: PO Box 829,<br>Larkvale, KS<br>Office: (620) 555-0176<br>Fax: (620) 555-0134<br>Email: vgroup@tqx.example</p>
    </div>
    <div class="assoc">
      <h5>Associate with</h5>
      <div class="assoc-row"><span class="nl">Gavel Row</span><div class="badge"></div></div>
      <h5>Payment Mode</h5>
      <div class="cards"><i></i><i></i><i></i></div>
    </div>
    <div>
      <h5>Contact Us</h5>
      <p>Ph: (250) 555-0147<br>Ph: (250) 555-0193<br>Ph: (250) 555-0128<br>Email: lkr@fernvale-mail.example</p>
    </div>
  </div>
  <div class="footer-brand"><span class="brand-mark"></span><span class="brand-name">Whitcombe's Auction Mart Ltd.</span></div>
  <div class="footer-bottom">Copyright © 2014 · All Rights Reserved · Privacy Policy</div>
</footer>

</body>
</html>
```